Website design for company that sells taximeters and has a taxi dispatch call center, webstore neede

Need a website with a shop with at least 20 articles, in two languages, possibly by using a purchased theme (not purchased yet).The company provides equipments and dispatch solutions for taxi companies. Typical yellow and black theme

Target Market(s)

Taxi companies

Industry/Entity Type

Taxi

Number of Pages Required

3 page

Font styles to use
Sans Serif

Colors
fbed22
000000

Requirements
Must have
• - webstore for at least 20 articles
• - Documents folder where to put pdf material related to taximeters
• - contact form message submission
Nice to have
• Feedback section
Should not have
• Blogs,

```html
<!DOCTYPE html>
<html lang="en">
<head>
<meta charset="utf-8">
<title>Caborix – Taxi Meters &amp; Dispatch</title>
<link href="https://fonts.googleapis.com/css2?family=Montserrat:wght@400;600;700;800;900&family=Raleway:wght@400;500;600;700&display=swap" rel="stylesheet">
<style>
:root{
  --yellow:#f7e017;
  --black:#000;
  --ink:#1d1d1d;
  --graphite:#464a4a;
  --white:#fff;
  --muted:#8b8b8b;
  --line:#d6d6d6;
}
*{box-sizing:border-box;margin:0;padding:0}
html,body{width:1200px;height:3689px;overflow:hidden}
body{font-family:"Raleway",sans-serif;color:var(--ink);background:var(--white);position:relative}
a{color:inherit;text-decoration:none}

/* top bar */
.topbar{height:32px;background:var(--black);color:var(--white);font-size:13px;font-weight:600;position:relative}
.topbar .call{position:absolute;left:447px;top:8px}
.topbar .auth{position:absolute;left:704px;top:8px;display:flex;gap:28px}
.topbar .pickers{position:absolute;left:876px;top:4px;display:flex;gap:6px}
.picker{background:var(--white);color:var(--ink);height:24px;padding:0 10px;display:flex;align-items:center;gap:6px;font-size:11px;min-width:88px}
.picker .sq{width:12px;height:9px;background:#2a4a9a}

/* header */
.header{height:66px;background:var(--white);position:relative;border-bottom:1px solid #eee}
.brand{position:absolute;left:78px;top:12px;font-family:"Montserrat",sans-serif;font-weight:900;font-size:42px;letter-spacing:1px;color:var(--yellow)}
.nav{position:absolute;left:690px;top:20px;display:flex;gap:44px;font-family:"Montserrat",sans-serif;font-size:19px;color:#777}
.nav .active{color:var(--ink)}
.search{position:absolute;left:990px;top:18px;width:178px;height:30px;border:1px solid var(--line);font-size:12px;color:#aaa;padding:7px 10px}
.search svg{position:absolute;right:8px;top:8px}

/* hero */
.hero{height:627px;position:relative;background:radial-gradient(ellipse at 55% 45%,#5a4f3a 0%,#3a342a 45%,#1f1d19 100%);color:var(--white)}
.hero .photo{position:absolute;inset:0}
.hero-copy{position:absolute;left:138px;top:222px;width:660px}
.hero h1{font-family:"Montserrat",sans-serif;font-weight:900;font-size:39px;color:var(--yellow);letter-spacing:.5px;white-space:nowrap}
.hero h2{font-family:"Raleway",sans-serif;font-weight:500;font-size:24px;color:var(--yellow);margin-top:4px;white-space:nowrap}
.hero p{font-size:15px;line-height:20px;margin-top:12px;width:610px}
.hero .dots{position:absolute;left:1102px;top:224px;display:flex;flex-direction:column;gap:9px}
.hero .dots span{width:6px;height:6px;border-radius:50%;background:#6e8aa0}
.hero .dots span:first-child{background:#59b7e8}
.scroll{position:absolute;left:630px;top:445px;text-align:center}

/* call band */
.call-band{height:234px;background:var(--graphite);position:relative}
.call-band h2{position:absolute;left:226px;top:92px;font-family:"Montserrat",sans-serif;font-weight:900;font-size:42px;color:var(--white)}
.call-art{position:absolute;left:529px;top:12px;width:370px;height:222px;background:radial-gradient(circle at 50% 55%,#6c8a9a 0%,#566265 55%,#474a4a 80%);border-radius:8px}

/* deal */
.deal{height:521px;background:var(--yellow);position:relative}
.deal-copy{position:absolute;left:234px;top:78px;width:280px}
.deal .kicker{font-family:"Montserrat",sans-serif;font-size:11px;font-weight:600;letter-spacing:.5px}
.deal .kicker b{font-weight:800}
.deal h2{font-family:"Montserrat",sans-serif;font-weight:800;font-size:38px;line-height:38px;margin-top:14px}
.deal h2 span{color:#7a6f1a;font-weight:600}
.deal .note{font-size:10px;line-height:15px;margin-top:14px;width:240px}
.deal .expires{font-family:"Montserrat",sans-serif;font-size:10px;font-weight:800;margin-top:20px}
.count{display:flex;gap:22px;margin-top:12px}
.count div{text-align:center}
.count .box{width:44px;height:48px;background:var(--white);font-family:"Montserrat",sans-serif;font-weight:700;font-size:18px;display:flex;align-items:center;justify-content:center}
.count small{font-size:8px;display:block;margin-top:6px}
.btn-outline{display:inline-block;border:2px solid var(--black);font-family:"Montserrat",sans-serif;font-weight:700;font-size:10px;padding:10px 20px;margin-top:28px}
.deal-art{position:absolute;left:541px;top:74px;width:492px;height:295px;border-radius:40px;background:radial-gradient(ellipse at 45% 40%,#f3c92a 0%,#e8d85a 35%,#f2ecc8 60%,rgba(247,224,23,0) 78%)}

/* products */
.products{height:972px;position:relative;text-align:center}
.products h2{position:absolute;left:0;right:0;top:103px;font-family:"Montserrat",sans-serif;font-weight:400;font-size:21px;letter-spacing:1px}
.products h2 b{font-weight:800}
.tabs{position:absolute;left:0;right:0;top:144px;display:flex;justify-content:center;gap:28px;font-family:"Montserrat",sans-serif;font-size:10px;font-weight:700}
.tabs span:first-child{color:var(--muted);font-weight:600}
.tabs i{font-style:normal;color:#999}
.card{position:absolute;width:168px}
.card .img{height:221px;background:linear-gradient(180deg,#eeeeee 0%,#e2e2e2 55%,#f3f3f3 100%);position:relative}
.card .img::after{content:"";position:absolute;left:18px;right:18px;top:72px;height:82px;background:linear-gradient(180deg,#2b2b2b,#111);border-radius:6px}
.card .name{font-family:"Montserrat",sans-serif;font-size:8px;font-weight:700;margin-top:20px}
.card .name.muted{color:var(--muted);font-weight:500}
.card .price{font-size:13px;margin-top:6px}
.card .price s{font-size:9px;color:#999;margin-left:3px}
.card .actions{display:flex;gap:6px;justify-content:center;margin-top:10px}
.card .add{border:1px solid #555;font-family:"Montserrat",sans-serif;font-size:8px;font-weight:700;padding:6px 10px}
.card .add.dark{background:var(--ink);color:var(--white)}
.card .ico{width:24px;height:24px;border:1px solid #999;display:flex;align-items:center;justify-content:center}

/* footer */
.footer{height:1237px;background:var(--graphite);color:var(--white);position:relative}
.footer h2{position:absolute;left:0;right:0;top:80px;text-align:center;font-family:"Montserrat",sans-serif;font-weight:900;font-size:40px;color:var(--yellow);letter-spacing:1px}
.col{position:absolute;top:197px;font-size:11px;line-height:19px}
.col h4{font-family:"Montserrat",sans-serif;font-weight:800;font-size:11px;margin-bottom:2px}
.social{display:flex;gap:12px;margin-top:4px}
.social span{width:10px;height:10px;border-radius:50%;background:var(--white)}
.map{position:absolute;left:288px;top:394px;width:673px;height:315px;background:linear-gradient(135deg,#d8d8d8,#c6c6c6 50%,#d2d2d2)}
.field{position:absolute;border:1px solid #7a7e7e;font-size:11px;color:var(--yellow);padding:11px 14px}
.send{position:absolute;left:600px;top:1000px;width:100px;height:38px;background:var(--yellow);color:var(--white);font-family:"Montserrat",sans-serif;font-weight:700;font-size:11px;display:flex;align-items:center;justify-content:center}
.copy{position:absolute;left:0;right:0;top:1150px;text-align:center;font-family:"Montserrat",sans-serif;font-weight:700;font-size:11px}
</style>
</head>
<body>

<div class="topbar">
  <span class="call">Call Us Now : 555-014-2290</span>
  <div class="auth"><a href="#">Register</a><a href="#">Sign In</a></div>
  <div class="pickers">
    <div class="picker"><svg width="12" height="11" viewBox="0 0 12 11"><path d="M0 1h2l2 6h6l1-4H3" fill="none" stroke="#222" stroke-width="1.2"/><circle cx="5" cy="9.5" r="1" fill="#222"/><circle cx="9" cy="9.5" r="1" fill="#222"/></svg>empty</div>
    <div class="picker"><span class="sq"></span>English</div>
    <div class="picker">$ Dollar</div>
  </div>
</div>

<header class="header">
  <div class="brand">CABORIX</div>
  <nav class="nav"><a class="active" href="#">HOME</a><a href="#">ABOUT</a><a href="#">SHOP</a></nav>
  <div class="search">Search...<svg width="12" height="12" viewBox="0 0 12 12"><circle cx="5" cy="5" r="3.8" fill="none" stroke="#666" stroke-width="1.4"/><path d="M8 8l3 3" stroke="#666" stroke-width="1.4"/></svg></div>
</header>

<section class="hero">
  <div class="photo" role="img" aria-label="Dark close-up photo of an illuminated taxi roof sign at night"></div>
  <div class="hero-copy">
    <h1>BUYING TAXI METERS?</h1>
    <h2>installing a taxi meter or receipt printer into your taxi?</h2>
    <p>dedicated taxi services a taxi meter or receipt printer into your taxi?to full taxi branding, including taxi?roofsigns, branding, signage and CCTV Scanpoint?also have our own shop for all the taxi accessories you could ever need.</p>
  </div>
  <div class="dots"><span></span><span></span><span></span><span></span></div>
  <div class="scroll">
    <svg width="30" height="60" viewBox="0 0 30 60"><rect x="7" y="2" width="16" height="26" rx="8" fill="none" stroke="#fff" stroke-width="2"/><line x1="15" y1="8" x2="15" y2="13" stroke="#fff" stroke-width="2"/><path d="M10 36l5 5 5-5" fill="none" stroke="#fff" stroke-width="1.5"/></svg>
  </div>
</section>

<section class="call-band">
  <h2>CALL US:</h2>
  <div class="call-art" role="img" aria-label="Illustration of a call-center operator with headset, speech bubbles and 24-hour phone symbol"></div>
</section>

<section class="deal">
  <div class="deal-copy">
    <div class="kicker">WOW / SUPER DEAL <b>ONLY TODAY</b></div>
    <h2>TAXI SET<br>JUST <span>$35</span></h2>
    <p class="note">For happy fastest day, we're glad to notice you that we have open stage sale up to 70% only today for Taxi Gift Set with just $35. Grab it now!</p>
    <div class="expires">EXPIRES IN</div>
    <div class="count">
      <div><div class="box">09</div><small>Hours</small></div>
      <div><div class="box">45</div><small>Minutes</small></div>
      <div><div class="box">28</div><small>Seconds</small></div>
    </div>
    <a class="btn-outline" href="#">SHOP NOW</a>
  </div>
  <div class="deal-art" role="img" aria-label="Product photo of a yellow and a white taxi roof sign"></div>
</section>

<section class="products">
  <h2>AWESOME <b>OUR PRODUCTS</b></h2>
  <div class="tabs"><span>MOST POPULAR</span><i>|</i><span>BEST SELLER</span><i>|</i><span>NEW ARRIVAL</span></div>

  <div class="card" style="left:239px;top:192px"><div class="img" role="img" aria-label="Taxi meter product photo"></div><div class="name muted">TAXI METER</div><div class="price">$12.00</div><div class="actions"><span class="add dark">ADD TO CART</span><span class="ico"><svg width="10" height="9" viewBox="0 0 10 9"><path d="M5 8L1 4a2 2 0 014-2 2 2 0 014 2z" fill="none" stroke="#555"/></svg></span><span class="ico"><svg width="10" height="10" viewBox="0 0 10 10"><circle cx="5" cy="5" r="3.5" fill="none" stroke="#555"/></svg></span></div></div>
  <div class="card" style="left:425px;top:192px"><div class="img" role="img" aria-label="Taxi meter product photo"></div><div class="name">TAXI METER</div><div class="price">$10.20<s>$18.20</s></div><div class="actions"><span class="add">ADD TO CART</span><span class="ico"><svg width="10" height="9" viewBox="0 0 10 9"><path d="M5 8L1 4a2 2 0 014-2 2 2 0 014 2z" fill="none" stroke="#555"/></svg></span><span class="ico"><svg width="10" height="10" viewBox="0 0 10 10"><circle cx="5" cy="5" r="3.5" fill="none" stroke="#555"/></svg></span></div></div>
  <div class="card" style="left:615px;top:192px"><div class="img" role="img" aria-label="Taxi meter product photo"></div><div class="name">TAXI METER</div><div class="price">$45.50</div><div class="actions"><span class="add">ADD TO CART</span><span class="ico"><svg width="10" height="9" viewBox="0 0 10 9"><path d="M5 8L1 4a2 2 0 014-2 2 2 0 014 2z" fill="none" stroke="#555"/></svg></span><span class="ico"><svg width="10" height="10" viewBox="0 0 10 10"><circle cx="5" cy="5" r="3.5" fill="none" stroke="#555"/></svg></span></div></div>
  <div class="card" style="left:802px;top:192px"><div class="img" role="img" aria-label="Taxi meter product photo"></div><div class="name">TAXI METER</div><div class="price">$25.60<s>$30.00</s></div><div class="actions"><span class="add">ADD TO CART</span><span class="ico"><svg width="10" height="9" viewBox="0 0 10 9"><path d="M5 8L1 4a2 2 0 014-2 2 2 0 014 2z" fill="none" stroke="#555"/></svg></span><span class="ico"><svg width="10" height="10" viewBox="0 0 10 10"><circle cx="5" cy="5" r="3.5" fill="none" stroke="#555"/></svg></span></div></div>

  <div class="card" style="left:239px;top:529px"><div class="img" role="img" aria-label="Taxi meter product photo"></div><div class="name">TAXI METER</div><div class="price">$25.50</div><div class="actions"><span class="add">ADD TO CART</span><span class="ico"><svg width="10" height="9" viewBox="0 0 10 9"><path d="M5 8L1 4a2 2 0 014-2 2 2 0 014 2z" fill="none" stroke="#555"/></svg></span><span class="ico"><svg width="10" height="10" viewBox="0 0 10 10"><circle cx="5" cy="5" r="3.5" fill="none" stroke="#555"/></svg></span></div></div>
  <div class="card" style="left:425px;top:529px"><div class="img" role="img" aria-label="Taxi meter product photo"></div><div class="name">TAXI METER</div><div class="price">$23.00</div><div class="actions"><span class="add">ADD TO CART</span><span class="ico"><svg width="10" height="9" viewBox="0 0 10 9"><path d="M5 8L1 4a2 2 0 014-2 2 2 0 014 2z" fill="none" stroke="#555"/></svg></span><span class="ico"><svg width="10" height="10" viewBox="0 0 10 10"><circle cx="5" cy="5" r="3.5" fill="none" stroke="#555"/></svg></span></div></div>
  <div class="card" style="left:615px;top:529px"><div class="img" role="img" aria-label="Taxi meter product photo"></div><div class="name">TAXI METER</div><div class="price">$20.00</div><div class="actions"><span class="add">ADD TO CART</span><span class="ico"><svg width="10" height="9" viewBox="0 0 10 9"><path d="M5 8L1 4a2 2 0 014-2 2 2 0 014 2z" fill="none" stroke="#555"/></svg></span><span class="ico"><svg width="10" height="10" viewBox="0 0 10 10"><circle cx="5" cy="5" r="3.5" fill="none" stroke="#555"/></svg></span></div></div>
  <div class="card" style="left:802px;top:529px"><div class="img" role="img" aria-label="Taxi meter product photo"></div><div class="name">TAXI METER</div><div class="price">$21.00</div><div class="actions"><span class="add">ADD TO CART</span><span class="ico"><svg width="10" height="9" viewBox="0 0 10 9"><path d="M5 8L1 4a2 2 0 014-2 2 2 0 014 2z" fill="none" stroke="#555"/></svg></span><span class="ico"><svg width="10" height="10" viewBox="0 0 10 10"><circle cx="5" cy="5" r="3.5" fill="none" stroke="#555"/></svg></span></div></div>
</section>

<footer class="footer">
  <h2>GET IN TOUCH</h2>
  <div class="col" style="left:285px"><h4>QUICK LINKS</h4>About us<br>Contact us<br>Meters</div>
  <div class="col" style="left:438px"><h4>LEGAL</h4>Privacy Policy<br>Cookie Policy<br>Terms and Conditions with guarantee<br>Cancellations &amp; Refunds<br>Website Terms of use<br>Modern Slavery Compliance</div>
  <div class="col" style="left:664px"><h4>TRADE &amp; BUSINESS</h4>Traders &amp; Associates</div>
  <div class="col" style="left:861px"><h4>SOZIAL</h4><div class="social"><span></span><span></span><span></span><span></span></div></div>
  <div class="map" role="img" aria-label="Grey street map showing the company location"></div>
  <div class="field" style="left:381px;top:784px;width:258px;height:40px">Your Name</div>
  <div class="field" style="left:656px;top:784px;width:264px;height:40px">Your Email</div>
  <div class="field" style="left:381px;top:838px;width:539px;height:123px">Your Message</div>
  <div class="send">SEND</div>
  <div class="copy">© 2018 caborix.net</div>
</footer>

</body>
</html>
```